UK landscaping company needs website

We, Brackwell Landscapes need a website design for a company based in Surrey, UK. The design should be bold and playful. We have three main areas of work driveways, paving and fencing. It shouldn't be too heavy in text and concentrate on the pictures from previous jobs we've completed. You may use stock images for the design, these can be changed if you are successful. Please don’t just copy the flyer it is just there to provide content.
We have a logo design which we would also like editing slightly.
Here are some of my local competitors
https://www.fernivalelandscapes.co.uk/

https://www.twinbirchgardendesign.com/

https://mallowbecklandscapes.co.uk/

Industry/Entity Type

Landscaping

Coding

Coded - Design and coding required

Number of Pages Required

3 page

Font styles to use
Sans Serif

Requirements
Must have
• Pictures of my previous jobs.
Must be mobile friendly
Easy to navigate
Nice to have
• Try to use different colours. It would be good to have some designs that aren’t just black and green.
I’d like some curves in the design.
Should not have
• We install hard landscaping. Think more building/construction and less plants and cutting grass.

```html
<!DOCTYPE html>
<html lang="en">
<head>
<meta charset="utf-8">
<title>Brackwell Landscapes</title>
<link rel="stylesheet" href="https://fonts.googleapis.com/css2?family=Poppins:wght@400;500;600;700&display=swap">
<style>
:root{
  --green:#6fbf44;
  --green-dark:#58a72f;
  --black:#000;
  --white:#fff;
  --ink:#111;
  --muted:#444;
  --placeholder:#c4c4c4;
}
*{box-sizing:border-box;margin:0;padding:0}
html,body{width:1200px;height:3125px;overflow:hidden}
body{font-family:'Poppins',sans-serif;color:var(--ink);background:var(--white);position:relative}
.abs{position:absolute}
.photo{position:absolute}

/* top bar */
.top-bar{position:absolute;top:0;left:0;width:1200px;height:20px;background:var(--green);color:var(--white);font-size:8px}
.top-bar .tagline{position:absolute;left:227px;top:5px}
.top-bar .hours{position:absolute;right:226px;top:5px}

/* header */
.site-header{position:absolute;top:20px;left:0;width:1200px;height:77px;background:var(--black);color:var(--white)}
.brand{position:absolute;left:227px;top:18px;font-weight:700;font-size:20px;line-height:1;letter-spacing:.5px}
.brand small{display:block;font-size:9px;letter-spacing:2px;margin-top:4px;font-weight:700}
.contact-item{position:absolute;top:17px;display:flex;align-items:center;gap:8px}
.contact-item .ic{width:26px;height:26px;border:2px solid var(--green);border-radius:50%;display:flex;align-items:center;justify-content:center}
.contact-item .lbl{font-size:7px;color:var(--green);line-height:1.1}
.contact-item .val{font-size:13px;line-height:1.2}
.contact-item.phone{left:428px}
.contact-item.email{left:623px}
.socials{position:absolute;display:flex;gap:9px}
.socials span{width:21px;height:21px;border-radius:50%;background:var(--green);display:block}
.site-header .socials{right:226px;top:23px}
.main-nav{position:absolute;left:593px;top:87px;width:381px;height:19px;background:var(--green);border-radius:9px;display:flex;justify-content:space-around;align-items:center;font-size:10px;color:var(--white);z-index:3;padding:0 8px}

/* hero */
.hero{position:absolute;top:97px;left:0;width:1200px;height:470px;overflow:hidden}
.hero .photo{inset:0;background:linear-gradient(135deg,#c9a772 0%,#d9b887 22%,#5d8f2c 40%,#3f7020 65%,#6c9a3d 100%)}
.hero .shade{position:absolute;inset:0;background:rgba(0,0,0,.22)}
.hero h1{position:absolute;top:136px;left:0;width:1200px;text-align:center;color:var(--white);font-size:23px;font-weight:600;line-height:29px}
.hero p{position:absolute;top:200px;left:0;width:1200px;text-align:center;color:var(--white);font-size:13px;line-height:17px}
.hero .actions{position:absolute;top:251px;left:0;width:1200px;display:flex;justify-content:center;gap:17px}
.btn{display:inline-flex;align-items:center;justify-content:center;font-weight:600;text-transform:uppercase;color:var(--white)}
.btn-green{background:var(--green);border-radius:3px}
.btn-outline{border:2px solid var(--white);border-radius:3px}
.hero .btn{height:32px;width:92px;font-size:10px}
.hero .arrow{position:absolute;top:180px}
.hero-curve{position:absolute;left:0;bottom:0;width:1200px;height:100px}

/* about */
.about{position:absolute;top:558px;left:0;width:1200px;height:370px;background:var(--black);color:var(--white)}
.about h2{position:absolute;left:228px;top:16px;color:var(--green);font-size:21px;font-weight:600}
.about .copy{position:absolute;left:227px;top:55px;width:375px;font-size:13px;line-height:18.6px}
.about .copy p+p{margin-top:18px}
.about .btn{position:absolute;left:227px;top:257px;width:92px;height:32px;font-size:11px}
.about .photo{left:652px;top:50px;width:322px;height:241px;border:2px solid var(--green);background:linear-gradient(160deg,#a6a9a2 0%,#c9b9a0 40%,#b8a58b 70%,#6b9a3c 100%)}

/* services */
.services{position:absolute;top:928px;left:0;width:1200px;height:835px;background:var(--white)}
.section-title{text-transform:uppercase;font-weight:600;font-size:21px;text-align:center}
.services .section-title{position:absolute;top:50px;width:1200px}
.service{position:absolute;width:220px;text-align:center}
.service .thumb{width:167px;height:167px;margin:0 auto;border-radius:50%;border:5px solid var(--green);padding:4px;background:var(--white)}
.service .thumb div{width:100%;height:100%;border-radius:50%}
.service h3{font-size:14px;font-weight:600;margin-top:20px;text-transform:uppercase}
.service p{font-size:11.5px;line-height:18.8px;color:var(--muted);margin-top:6px}

/* projects */
.projects{position:absolute;top:1763px;left:0;width:1200px;height:368px;background:var(--green)}
.projects .section-title{position:absolute;top:34px;width:1200px}
.project{position:absolute;top:92px;width:235px;height:176px;border:3px solid var(--white)}
.projects .btn{position:absolute;left:534px;top:303px;width:133px;height:40px;background:var(--black);border-radius:3px;font-size:13px}

/* contact */
.contact-intro{position:absolute;top:2192px;left:0;width:1200px;text-align:center;font-size:20px;font-weight:600;line-height:26px;text-transform:uppercase}
.contact-form{position:absolute;left:199px;top:2326px;width:798px;height:404px;background:var(--black);border-radius:16px}
.field{position:absolute;background:var(--white);border-radius:3px;color:var(--placeholder);font-size:14px;padding:10px 13px;height:42px}
.contact-form .btn{position:absolute;left:38px;top:320px;width:126px;height:38px;font-size:13px}

/* grass + footer */
.grass{position:absolute;top:2770px;left:0;width:1200px;height:276px;background:linear-gradient(180deg,#ffffff 0%,#d9efc4 25%,#8fcf4f 60%,#4f9a22 100%)}
.site-footer{position:absolute;top:3045px;left:0;width:1200px;height:61px;background:var(--black);color:var(--white)}
.site-footer .brand{top:16px;font-size:17px}
.site-footer .brand small{font-size:7px;margin-top:2px}
.footer-nav{position:absolute;left:420px;top:22px;display:flex;gap:23px;font-size:12px;font-weight:500}
.site-footer .socials{right:226px;top:20px}
.copyright{position:absolute;top:3106px;left:0;width:1200px;height:19px;background:var(--green);color:var(--white);font-size:8px;text-align:center;line-height:19px}
</style>
</head>
<body>

<div class="top-bar">
  <span class="tagline">We offer stone landscaping, maintenance and design for residential, commercial and industrial clients.</span>
  <span class="hours">Mon-Sat 8.00 - 18.00 &nbsp;|&nbsp; Sunday Closed</span>
</div>

<header class="site-header">
  <div class="brand">BRACKWELL<small>LANDSCAPES</small></div>
  <div class="contact-item phone">
    <span class="ic"><svg width="12" height="12" viewBox="0 0 24 24"><path d="M6.6 10.8a15 15 0 0 0 6.6 6.6l2.2-2.2c.3-.3.7-.4 1-.2 1.1.4 2.3.6 3.6.6.6 0 1 .4 1 1V20c0 .6-.4 1-1 1C10.6 21 3 13.4 3 4c0-.6.4-1 1-1h3.5c.6 0 1 .4 1 1 0 1.3.2 2.5.6 3.6.1.3 0 .7-.2 1z" fill="#6fbf44"/></svg></span>
    <div><div class="lbl">CALL US FOR FEE ESTIMATE</div><div class="val">07700 481 256</div></div>
  </div>
  <div class="contact-item email">
    <span class="ic"><svg width="12" height="10" viewBox="0 0 24 18"><rect x="1" y="1" width="22" height="16" rx="2" fill="none" stroke="#6fbf44" stroke-width="2"/><path d="M1 2l11 8 11-8" fill="none" stroke="#6fbf44" stroke-width="2"/></svg></span>
    <div><div class="lbl">EMAIL US FOR MORE DETAILS</div><div class="val">info@brackwell-landscapes.com</div></div>
  </div>
  <div class="socials"><span></span><span></span><span></span></div>
</header>

<nav class="main-nav"><span>Home</span><span>About Us</span><span>Our Services</span><span>Gallery</span><span>Contact Us</span></nav>

<section class="hero">
  <div class="photo" role="img" aria-label="Finished garden with timber decking, raised lawn and sandstone patio"></div>
  <div class="shade"></div>
  <svg class="arrow" style="left:130px" width="14" height="30" viewBox="0 0 14 30"><path d="M12 2L2 15l10 13" fill="none" stroke="rgba(255,255,255,.35)" stroke-width="1.5"/></svg>
  <svg class="arrow" style="left:1050px" width="14" height="30" viewBox="0 0 14 30"><path d="M2 2l10 13L2 28" fill="none" stroke="rgba(255,255,255,.7)" stroke-width="1.5"/></svg>
  <h1>PROFESSIONAL STONE GARDENING, LANDSCAPING<br>&amp; MAINTENANCE SERVICES</h1>
  <p>By creating an outdoor environment, you’re essentially building “rooms” that are<br>functional, unique and fun</p>
  <div class="actions"><span class="btn btn-green">Contact Us</span><span class="btn btn-outline">Read More</span></div>
  <svg class="hero-curve" viewBox="0 0 1200 100" preserveAspectRatio="none">
    <path d="M0 75 C120 30 260 5 420 25 C600 50 760 70 920 50 C1040 35 1130 12 1200 0 L1200 100 L0 100Z" fill="#6fbf44"/>
    <path d="M0 100 C120 60 260 38 420 45 C600 55 760 80 920 62 C1040 48 1130 25 1200 10 L1200 100Z" fill="#000"/>
  </svg>
</section>

<section class="about">
  <h2>ABOUT US</h2>
  <div class="copy">
    <p>We at Brackwell Landscapes are a professional, experienced landscaping business that delivers premium garden construction at an affordable price. We provide all aspects of hard and soft landscaping throughout Surrey and surrounding areas.</p>
    <p>We pride ourselves on excellent workmanship and attention to detail. Using only top quality materials to ensure an outstanding and long-lasting finish, installed using both traditional and modern techniques.</p>
  </div>
  <span class="btn btn-green">Read More</span>
  <div class="photo" role="img" aria-label="Circular sandstone patio in front of a garden room and lawn"></div>
</section>

<section class="services">
  <h2 class="section-title">Our Services</h2>
  <div class="service" style="left:241px;top:117px"><div class="thumb"><div role="img" aria-label="Grey slab driveway beside lawn" style="background:linear-gradient(160deg,#4c7f2b 0%,#9a9a96 35%,#c2c2bf 100%)"></div></div><h3>Driveways</h3><p>We at Brackwell Landscapes are a professional, experienced landscaping business that delivers premium garden construction</p></div>
  <div class="service" style="left:491px;top:117px"><div class="thumb"><div role="img" aria-label="Garden before and after a new lawn design" style="background:linear-gradient(180deg,#7a6c55 0%,#5b6a3e 45%,#5c9a32 55%,#4c8a2a 100%)"></div></div><h3>Garden Design</h3><p>We at Brackwell Landscapes are a professional, experienced landscaping business that delivers premium garden construction</p></div>
  <div class="service" style="left:743px;top:117px"><div class="thumb"><div role="img" aria-label="Dark block paved driveway" style="background:linear-gradient(160deg,#6b8f3f 0%,#5c5f63 30%,#45484c 100%)"></div></div><h3>Paving &amp; Brickwork</h3><p>We at Brackwell Landscapes are a professional, experienced landscaping business that delivers premium garden construction</p></div>
  <div class="service" style="left:241px;top:462px"><div class="thumb"><div role="img" aria-label="Planted borders and curved lawn" style="background:linear-gradient(170deg,#8a6d55 0%,#5f8d36 40%,#4d9c2e 100%)"></div></div><h3>Planting &amp; Turfing</h3><p>We at Brackwell Landscapes are a professional, experienced landscaping business that delivers premium garden construction</p></div>
  <div class="service" style="left:491px;top:462px"><div class="thumb"><div role="img" aria-label="Timber fencing and pergola over grey decking" style="background:linear-gradient(180deg,#8b7a68 0%,#7d6d5d 55%,#9a9ca0 100%)"></div></div><h3>Fencing &amp; Decking</h3><p>We at Brackwell Landscapes are a professional, experienced landscaping business that delivers premium garden construction</p></div>
  <div class="service" style="left:743px;top:462px"><div class="thumb"><div role="img" aria-label="Roll of artificial grass" style="background:radial-gradient(circle at 55% 60%,#2f3a2c 0%,#3d7a24 35%,#6fc03b 70%,#ffffff 100%)"></div></div><h3>Artificial Grass</h3><p>We at Brackwell Landscapes are a professional, experienced landscaping business that delivers premium garden construction</p></div>
</section>

<section class="projects">
  <h2 class="section-title">Our Projects</h2>
  <div class="project" style="left:229px;background:linear-gradient(180deg,#b9c3cb 0%,#5c4a3b 30%,#4b8a28 60%,#a89f95 100%)" role="img" aria-label="Fenced garden with timber steps, lawn and patio seating"></div>
  <div class="project" style="left:483px;background:linear-gradient(160deg,#8a7a63 0%,#5e9b33 35%,#a09088 65%,#8d8a86 100%)" role="img" aria-label="Lawn and wet paving between brick walls"></div>
  <div class="project" style="left:738px;background:linear-gradient(180deg,#5e6b4a 0%,#8d9a6c 25%,#d3d3d0 45%,#505660 100%)" role="img" aria-label="Dark porcelain patio with raised rendered planters"></div>
  <span class="btn">View More</span>
</section>

<div class="contact-intro">We’d love to hear from you. Call us at 07700 481 256<br>or send us a message using the form below and we’ll get back to you<br>as soon as we can.</div>

<form class="contact-form">
  <div class="field" style="left:38px;top:59px;width:338px">Name</div>
  <div class="field" style="left:419px;top:59px;width:339px">Email</div>
  <div class="field" style="left:38px;top:127px;width:338px">Phone</div>
  <div class="field" style="left:419px;top:127px;width:339px">Type of Services</div>
  <div class="field" style="left:38px;top:194px;width:720px;height:104px">Your Message</div>
  <span class="btn btn-green">Submit</span>
</form>

<div class="grass" role="img" aria-label="Close-up of tall green grass blades"></div>

<footer class="site-footer">
  <div class="brand">BRACKWELL<small>LANDSCAPES</small></div>
  <nav class="footer-nav"><span>Home</span><span>About Us</span><span>Our Services</span><span>Gallery</span><span>Contact Us</span></nav>
  <div class="socials"><span></span><span></span><span></span></div>
</footer>
<div class="copyright">Copyright © 2020 Brackwell Landscapes . All Rights Reserved</div>

</body>
</html>
```